Unique Elegant Stationary Set

Prepare a unique eye catching stationary set consisting of :
(1) Letterhead
(2) A3 Envelope
(3) Business Card
(4) Email Signature Banner

Package to be elegant, modern, and designers not only to think of design or colors but also materials could make a big difference, embossing, debossing, glossy, matt ....etc.

I attached both our new logos (Stacked or Linear) noting you may use any of them but you cant modify anything in the logos. Also attached our final draft portfolio to see what type of projects we work on and i also have here a glimmerboard page link showing the direction we want: https://www.glimmerboard.example/dorvanmelik/business-card-design/

Target Market(s)

VVIP / Elite Developers

Industry/Entity Type

Architecture

Font styles to use
Sans Serif
Other font styles liked:
• unitext

Requirements
Should not have
• too many colors, or being busy in general. We want something pleasing to the eye

```html
<!DOCTYPE html>
<html lang="en">
<head>
<meta charset="utf-8">
<title>Veltra Design — Stationery Set</title>
<link href="https://fonts.googleapis.com/css2?family=Montserrat:wght@400;500;600;700&family=Open+Sans:wght@400;600&display=swap" rel="stylesheet">
<style>
  :root {
    --bg: #2c333d;
    --ink-black: #1f1f20;
    --paper: #f3f3f2;
    --flap-grey: #a9a9aa;
    --brand-red: #c8161d;
    --silver: #b9bcc0;
    --text-dark: #2a2a2a;
    --text-mid: #555;
  }
  * { box-sizing: border-box; margin: 0; padding: 0; }
  html, body { width: 1200px; height: 889px; overflow: hidden; }
  body {
    background: var(--bg);
    font-family: "Montserrat", sans-serif;
    position: relative;
  }
  .piece { position: absolute; box-shadow: 0 10px 24px rgba(0,0,0,.35); }

  .wordmark { font-family: "Montserrat", sans-serif; font-weight: 700; letter-spacing: .08em; text-transform: uppercase; line-height: 1; }
  .wordmark--red { color: var(--brand-red); }
  .wordmark--silver { color: var(--silver); }

  /* Business card front */
  .card-front {
    left: 40px; top: 40px; width: 150px; height: 250px;
    background: var(--paper); padding: 18px 16px;
    display: flex; flex-direction: column;
  }
  .card-front__name { color: var(--brand-red); font-weight: 700; font-size: 10px; letter-spacing: .04em; text-transform: uppercase; }
  .card-front__role { font-size: 6.5px; font-weight: 600; letter-spacing: .06em; text-transform: uppercase; color: var(--text-dark); margin-top: 3px; }
  .card-front__details { margin-top: 16px; font-size: 6.5px; line-height: 1.6; color: var(--text-mid); text-transform: uppercase; }
  .card-front__logo { margin-top: auto; align-self: flex-end; font-size: 14px; }

  /* Business card back */
  .card-back {
    left: 220px; top: 90px; width: 260px; height: 150px;
    background: var(--ink-black);
    display: flex; align-items: center; justify-content: center;
  }
  .card-back .wordmark { font-size: 22px; }

  /* Envelope back */
  .envelope-back {
    left: 40px; top: 320px; width: 460px; height: 230px;
    background: var(--ink-black); overflow: hidden;
  }
  .envelope-back svg { position: absolute; inset: 0; }

  /* Envelope front */
  .envelope-front {
    left: 40px; top: 590px; width: 460px; height: 230px;
    background: var(--ink-black); padding: 22px 26px;
  }
  .envelope-front__address { color: #e8e8e8; font-size: 10px; line-height: 1.5; letter-spacing: .06em; text-transform: uppercase; }
  .envelope-front__logo { position: absolute; right: 26px; bottom: 26px; font-size: 22px; }

  /* Letterhead */
  .letterhead {
    left: 600px; top: 40px; width: 560px; height: 800px;
    background: var(--paper); padding: 48px 52px; overflow: hidden;
    font-family: "Open Sans", sans-serif; color: var(--text-dark);
  }
  .letterhead__logo { position: absolute; top: 48px; right: 52px; font-size: 26px; }
  .letterhead__contact {
    position: absolute; top: 110px; right: 52px; text-align: right;
    font-family: "Montserrat", sans-serif; font-size: 9px; line-height: 1.7; color: var(--text-mid); letter-spacing: .04em;
  }
  .letterhead__contact li { list-style: none; display: flex; gap: 6px; align-items: center; justify-content: flex-end; }
  .letterhead__contact svg { width: 9px; height: 9px; fill: var(--brand-red); }
  .letterhead__recipient { margin-top: 96px; font-size: 10px; line-height: 1.55; }
  .letterhead__salutation { margin-top: 22px; font-size: 10px; }
  .letterhead__body p { margin-top: 14px; font-size: 9.5px; line-height: 1.6; max-width: 420px; }
  .letterhead__closing { margin-top: 20px; font-size: 10px; }
  .letterhead__signatory { margin-top: 40px; font-size: 10px; line-height: 1.5; }
  .letterhead__watermark {
    position: absolute; left: 52px; bottom: 120px;
    font-size: 54px; color: rgba(0,0,0,.05);
  }
  .letterhead__footer {
    position: absolute; left: 52px; bottom: 44px;
    font-family: "Montserrat", sans-serif; font-size: 9px; line-height: 1.55; letter-spacing: .05em; text-transform: uppercase; color: var(--text-mid);
  }
</style>
</head>
<body>

  <section class="piece card-front" aria-label="Business card front">
    <p class="card-front__name">Marco Telden</p>
    <p class="card-front__role">Brand Manager</p>
    <p class="card-front__details">
      Halden Tower,<br>14th Floor, 1402<br>P.O. Box 40210<br>+971 2 555 0142<br>info@veltradesign.example<br>www.veltradesign.example
    </p>
    <p class="wordmark wordmark--red card-front__logo">Veltra Design</p>
  </section>

  <section class="piece card-back" aria-label="Business card back">
    <p class="wordmark wordmark--silver">Veltra Design</p>
  </section>

  <section class="piece envelope-back" aria-label="Envelope back with open flap">
    <svg viewBox="0 0 460 230" width="460" height="230">
      <polygon points="0,0 460,0 460,70 230,150 0,70" fill="var(--flap-grey)"/>
      <polygon points="0,70 230,150 460,70 460,230 0,230" fill="var(--ink-black)"/>
      <line x1="0" y1="70" x2="230" y2="150" stroke="#111" stroke-width="1"/>
      <line x1="460" y1="70" x2="230" y2="150" stroke="#111" stroke-width="1"/>
    </svg>
  </section>

  <section class="piece envelope-front" aria-label="Envelope front">
    <p class="envelope-front__address">Halden Tower,<br>14th Floor, 1402<br>P.O. Box: 40210</p>
    <p class="wordmark wordmark--silver envelope-front__logo">Veltra Design</p>
  </section>

  <article class="piece letterhead" aria-label="Letterhead">
    <p class="wordmark wordmark--red letterhead__logo">Veltra Design</p>
    <ul class="letterhead__contact">
      <li><svg viewBox="0 0 10 10"><path d="M2 0l2 2-1 1.5c.8 1.5 2 2.7 3.5 3.5L8 6l2 2-1.5 2C4 9.5.5 6 0 1.5z"/></svg>+971 2 555 0142</li>
      <li><svg viewBox="0 0 10 10"><path d="M0 2h10v6H0zM0 2l5 3.5L10 2"/></svg>info@veltradesign.example</li>
      <li><svg viewBox="0 0 10 10"><circle cx="5" cy="5" r="5"/></svg>www.veltradesign.example</li>
    </ul>

    <p class="letterhead__recipient">First Name Last Name<br>Addressee's name<br>Building number/name and street<br>Post Town, Post Code</p>
    <p class="letterhead__salutation">Dear First Name</p>
    <div class="letterhead__body">
      <p>Lorem ipsum dolor sit amet, consectetur adipiscing elit. Vestibulum eu vulputate sapien. In quis imperdiet lectus, eget accumsan sem. Vestibulum consequat rhoncus cursus. Quisque ultrices facilisis libero eu facilisis. Phasellus consequat justo mi, in sollicitudin justo sed eros blandit, non eleifend elit lacus. Nisl congue sit amet, facilisis at pulvinar eu, rutrum ut mauris. Suspendisse aliquam purus gravida, pulvinar elit. Aliquam erat volutpat. Sed vehicula diam leo, et vehicula leo elementum et. Duis nec suscipit justo. Maecenas iaculis sapien egestas. Quisque imperdiet ut quam ut placerat. Duis facilisis nisi sit amet dictum egestas, neque nulla elementum nibh, in ultrices mi magna nec metus.</p>
      <p>Duis arcu lacus, accumsan id lectus eu, condimentum tincidunt purus. Cras ac justo sed odio mattis gravida consectetur ac sapien. Integer eleifend enim et ipsum fermentum auctor. Quisque at porttitor velit. Aenean gravida nibh odio, eget tempus mauris semper at. In consectetur sed leo ut molestie. Sed pharetra urna quis turpis fringilla, ut posuere massa hendrerit. Proin pulvinar nibh augue, vel luctus elit aliquet non. Nunc elementum iaculis turpis eu interdum. Pellentesque non imperdiet magna, ut facilisis augue.</p>
    </div>
    <p class="letterhead__closing">Sincerely,</p>
    <p class="letterhead__signatory">First Name Last Name<br>Position</p>

    <p class="wordmark letterhead__watermark">Veltra</p>
    <p class="letterhead__footer">Halden Tower,<br>14th Floor, 1402<br>P.O. Box: 40210</p>
  </article>

</body>
</html>
```